Zorvik App Graphics Design

Our application promotes location based self expression via pictures and text. The primary focus of the application is on the content posted and not on the person that posted it.

We want a very clean and fresh design that evokes positive energy. Our site is unique so our design should be as well. People will reveal thoughts on our site, so the design should convey a "revealing" feel. Our site is a place where people are comfortable to freely express themselves. Colors we have in mind are blue and green hues with earth tones for background.

Our project is to design ten screens for our Zorvik application at resolution of 1136-by-640 pixels:

Feed Screen
Camera Screen
Post Screen
Check In Screen
Approval Screen
Map Screen
Flag Screen
Feed Select Screen
Export Screen
Menu Screen

In the contest phase we will require only three screens to be submitted. The screens we require to be submitted are: Feed Screen; Map Screen and Camera Screen. The designer we select as the winner of the competition will then complete the project and deliver a total of the ten screens described above in the handover phase.

We have attached a document below with detailed specs of each screen, we ask for your innovation to bring these screens to life through your design.
Updates

We want to clarify one aspect regarding the VISOR: the visor needs to be transparent so that when the picture scrolls underneath it, you can still see the picture underneath the visor.

Hi Everyone,

We have noticed that some designers need clarification regarding the visor element in the feed screen.
I have attached two examples to our brief area called:
Visor Example 1 and Visor Example 2

Please note that these are not the style we are looking for but are a good example to the concept of a Transparent Visor above the feed stream. We are looking for you guys to come up with a Visor concept that is consistent with the style of the design you are submitting.

Thanks,

Bo

Target Market(s)

People 17-40 who want to share their thought about the world around them.

Industry/Entity Type

Flag

Font styles to use
Sans Serif
Other font styles liked:
• We like “Helvetica New” or “Avenir” but are flexible

Requirements
Must have
• Visor component should look innovative.

```html
<!DOCTYPE html>
<html lang="en">
<head>
<meta charset="utf-8">
<title>Zorvik – Feed Screen</title>
<link href="https://fonts.googleapis.com/css2?family=Roboto+Condensed:wght@400;700&family=Open+Sans:wght@400&display=swap" rel="stylesheet">
<style>
  :root{
    --canvas:#ffffff;
    --status:#000000;
    --green:#5e8a00;
    --green-dark:#3f5e00;
    --visor:rgba(255,255,255,0.82);
    --title-blue:#1679b5;
    --btn-light:#55b6e0;
    --btn-dark:#1d77a6;
    --band-blue:#1b6e98;
    --tray:#e6e6e6;
    --white:#ffffff;
    --icon-dark:#1f2a10;
  }
  *{margin:0;padding:0;box-sizing:border-box}
  html,body{width:1000px;height:1200px;overflow:hidden;background:var(--canvas)}
  .screen{position:absolute;left:30px;top:32px;width:640px;height:1136px;overflow:hidden;font-family:"Roboto Condensed",Arial,sans-serif;background:var(--tray)}
  .status-bar{position:absolute;left:0;top:0;width:640px;height:40px;background:var(--status);color:#d8d8d8;font-family:"Open Sans",Arial,sans-serif;font-weight:600}
  .status-bar .carrier{position:absolute;left:8px;top:7px;font-size:22px;display:flex;align-items:center;gap:6px}
  .status-bar .time{position:absolute;left:0;width:640px;top:5px;text-align:center;font-size:24px}
  .status-bar .status-icons{position:absolute;right:8px;top:7px}
  .app-header{position:absolute;left:0;top:40px;width:640px;height:88px;background:var(--green);border-bottom:3px solid #eef2e6}
  .app-header h1{position:absolute;left:0;width:640px;top:20px;text-align:center;color:var(--white);font-size:40px;font-weight:700}
  .round-btn{position:absolute;top:23px;width:44px;height:44px;border-radius:50%;background:radial-gradient(circle at 40% 30%,#fafafa,#b9b9b9);box-shadow:0 1px 2px rgba(0,0,0,.4);display:flex;align-items:center;justify-content:center}
  .round-btn.menu{left:13px}
  .round-btn.search{right:13px}
  .post-photo{position:absolute;left:0;top:131px;width:640px;height:676px;background:linear-gradient(160deg,#efe8d6 0%,#b9895a 30%,#7a4a26 55%,#a56f40 75%,#5a3a22 100%)}
  .visor{position:absolute;left:0;top:131px;width:640px;height:94px;background:var(--visor);border-bottom:1px solid rgba(255,255,255,.6)}
  .visor h2{text-align:center;color:var(--title-blue);font-size:44px;font-weight:400;line-height:94px}
  .photo-action{position:absolute;top:255px;width:54px;height:54px;border-radius:50%;background:var(--white);border:2px solid #dfe6d6;display:flex;align-items:center;justify-content:center}
  .photo-action.flag{left:32px}
  .photo-action.share{left:555px}
  .post-meta{position:absolute;left:0;top:769px;width:640px;height:38px;background:rgba(40,30,25,.55);color:var(--white);font-family:"Open Sans",Arial,sans-serif;font-size:20px;line-height:38px}
  .post-meta .distance{position:absolute;left:20px}
  .post-meta .votes{position:absolute;left:0;width:640px;text-align:center}
  .post-meta .age{position:absolute;right:20px}
  .vote-btn{position:absolute;top:818px;width:305px;height:68px;border-radius:5px;background:var(--btn-light);box-shadow:0 3px 0 #2f7fa6;overflow:hidden}
  .vote-btn.promote{left:10px}
  .vote-btn.demote{left:325px}
  .vote-btn svg.tab{position:absolute;left:0;top:0}
  .vote-btn span{position:absolute;left:93px;top:0;line-height:68px;color:var(--white);font-size:36px}
  .location-band{position:absolute;left:0;top:898px;width:640px;height:56px;background:var(--band-blue);color:var(--white);font-size:17px;font-weight:700;padding:6px 10px;line-height:22px}
  .next-photo{position:absolute;left:0;top:955px;width:640px;height:80px;background:linear-gradient(180deg,#ded7c4 0%,#c9bfa4 45%,#8a6a3f 100%)}
  .tab-bar{position:absolute;left:0;top:1034px;width:640px;height:102px;background:var(--green);border-top:4px solid var(--green-dark)}
  .tab-item{position:absolute;top:10px;width:90px;text-align:center;color:var(--white);font-size:22px;font-weight:700}
  .tab-item.camera{left:18px}
  .tab-item.badge{left:531px}
  .tab-item svg{display:block;margin:0 auto 4px}
</style>
</head>
<body>
<div class="screen">
  <div class="status-bar">
    <div class="carrier">
      <svg width="36" height="18" viewBox="0 0 36 18"><g fill="#d8d8d8"><rect x="0" y="12" width="5" height="6"/><rect x="7" y="9" width="5" height="9"/><rect x="14" y="6" width="5" height="12"/><rect x="21" y="3" width="5" height="15"/><rect x="28" y="0" width="5" height="18"/></g></svg>
      Bet
    </div>
    <div class="time">4:20 PM</div>
    <svg class="status-icons" width="150" height="26" viewBox="0 0 150 26">
      <circle cx="13" cy="13" r="10" fill="#d8d8d8"/><path d="M13 7v6h4" stroke="#000" stroke-width="2" fill="none"/>
      <path d="M36 13l20-9-9 20-2-9z" fill="#d8d8d8"/>
      <circle cx="78" cy="13" r="11" fill="none" stroke="#d8d8d8" stroke-width="2.5"/><rect x="72" y="11" width="12" height="9" fill="#d8d8d8"/><path d="M74 11v-3a4 4 0 0 1 8 0v3" stroke="#d8d8d8" stroke-width="2" fill="none"/>
      <rect x="102" y="4" width="40" height="18" rx="3" fill="none" stroke="#d8d8d8" stroke-width="2"/><rect x="105" y="7" width="34" height="12" fill="#d8d8d8"/><rect x="143" y="9" width="3" height="8" fill="#d8d8d8"/>
    </svg>
  </div>

  <header class="app-header">
    <div class="round-btn menu"><svg width="22" height="18" viewBox="0 0 22 18"><g fill="#444"><rect y="1" width="22" height="4" rx="2"/><rect y="7" width="22" height="4" rx="2"/><rect y="13" width="22" height="4" rx="2"/></g></svg></div>
    <h1>Feed Name</h1>
    <div class="round-btn search"><svg width="22" height="22" viewBox="0 0 22 22"><circle cx="9" cy="9" r="6" stroke="#444" stroke-width="3" fill="none"/><path d="M13.5 13.5l6 6" stroke="#444" stroke-width="4" stroke-linecap="round"/></svg></div>
  </header>

  <div class="post-photo" role="img" aria-label="Photo of a bright kitchen with wooden cabinets, a marble island and bar stools"></div>

  <div class="visor"><h2>Beautiful Home</h2></div>

  <div class="photo-action flag"><svg width="28" height="28" viewBox="0 0 28 28"><path d="M6 4v22" stroke="#5e8a00" stroke-width="2.5"/><path d="M7 5c6-3 9 3 16 0v11c-7 3-10-3-16 0z" fill="#6f9a12"/></svg></div>
  <div class="photo-action share"><svg width="30" height="28" viewBox="0 0 30 28"><path d="M4 24c1-9 7-13 15-13V5l9 9-9 9v-6c-7 0-11 2-15 7z" fill="#6f9a12"/></svg></div>

  <div class="post-meta">
    <span class="distance">0.01 mi</span>
    <span class="votes">0</span>
    <span class="age">few hours ago</span>
  </div>

  <div class="vote-btn promote">
    <svg class="tab" width="90" height="68" viewBox="0 0 90 68"><path d="M0 0h74l14 34-14 34H0z" fill="var(--btn-dark)"/><circle cx="32" cy="34" r="15" fill="none" stroke="#fff" stroke-width="2.5"/><circle cx="27" cy="30" r="1.8" fill="#fff"/><circle cx="37" cy="30" r="1.8" fill="#fff"/><path d="M25 37q7 7 14 0" stroke="#fff" stroke-width="2.2" fill="none"/></svg>
    <span>Promote</span>
  </div>
  <div class="vote-btn demote">
    <svg class="tab" width="90" height="68" viewBox="0 0 90 68"><path d="M0 0h74l14 34-14 34H0z" fill="var(--btn-dark)"/><circle cx="32" cy="34" r="15" fill="none" stroke="#fff" stroke-width="2.5"/><circle cx="27" cy="30" r="1.8" fill="#fff"/><circle cx="37" cy="30" r="1.8" fill="#fff"/><path d="M25 42q7-7 14 0" stroke="#fff" stroke-width="2.2" fill="none"/></svg>
    <span>Demote</span>
  </div>

  <div class="location-band">Maple Diner,<br>48 Orchard Lane, Brookfield, NY 10231</div>

  <div class="next-photo" role="img" aria-label="Photo of a room with draped curtains and tall windows"></div>

  <nav class="tab-bar">
    <div class="tab-item camera">
      <svg width="54" height="42" viewBox="0 0 54 42"><path d="M4 8h12l4-6h14l4 6h12v32H4z" fill="var(--icon-dark)"/><circle cx="29" cy="24" r="11" fill="none" stroke="#5e8a00" stroke-width="3"/><circle cx="29" cy="24" r="5" fill="#5e8a00"/><rect x="8" y="4" width="6" height="3" fill="var(--icon-dark)"/></svg>
      Camera
    </div>
    <div class="tab-item badge">
      <svg width="44" height="44" viewBox="0 0 44 44"><path d="M22 2l4 4 5-2 2 5 5 1-1 5 4 4-4 4 1 5-5 1-2 5-5-2-4 4-4-4-5 2-2-5-5-1 1-5-4-4 4-4-1-5 5-1 2-5 5 2z" fill="var(--icon-dark)"/><circle cx="22" cy="20" r="7" fill="#5e8a00"/><path d="M14 32l-4 10 6-3 3 5 3-8M30 32l4 10-6-3-3 5-3-8" fill="var(--icon-dark)"/></svg>
      Badge
    </div>
  </nav>
</div>
</body>
</html>
```